PELMIR - Letterhead

Brightwater Institute of Letters and Crafts (PELMIR) is a non-profit organization that operates two tuition-free public schools - PELMIR Elementary for grades K to 5th and PELMIR College Prep for grades 6-12.

We are looking for a letterhead primarily to be used on Google Docs and Microsoft Word. Attached are two versions of our logo. One with our name spelled out and one with the acronym.

For Letterhead, we would like 3 addresses listed:

PELMIR HQ
41827 Heron Bluff Lane, Suite 316
Fernhollow, CA 90418

PELMIR Elementary (K-5)
57314 Marbleton Ridge Road
Fernhollow, CA 90418

PELMIR College Prep (6-12)
46803 Sable Creek Way
Cresthaven Mesa, CA 90436

Our Phone Number is (555) 555-0147
Our Fax Number is the same (555) 555-0147

Our website is www.pelmir-learn.example

Target Market(s)

Education

Industry/Entity Type

Education

Font styles to use
Sans Serif

Colors
0054AA
0677BA
7BADD7
CADEEF
E8F1F8

Requirements
Must have
• Logo, Address, Phone Number, Website.
Nice to have
• Modern and clean design.
Should not have
• Prefer that there is no bleed -- the letterhead will mostly be used in PDF format however sometimes it will be printed and our printers can not do a full bleed

```html
<!DOCTYPE html>
<html lang="en">
<head>
<meta charset="utf-8">
<title>PELMIR Letterhead</title>
<link rel="stylesheet" href="https://fonts.googleapis.com/css2?family=Arimo:wght@400;700&display=swap">
<style>
  :root {
    --navy: #0054AA;
    --blue: #0677BA;
    --sky: #7BADD7;
    --mist: #CADEEF;
    --frost: #E8F1F8;
    --paper: #ffffff;
    --backdrop: #eeeff1;
    --dot-grey: #dcdcdf;
  }
  * { margin: 0; padding: 0; box-sizing: border-box; }
  html, body {
    width: 1200px; height: 905px; overflow: hidden;
    background: var(--backdrop);
    font-family: "Arimo", Arial, sans-serif;
  }
  .letterhead {
    position: absolute;
    left: 266px; top: 20px;
    width: 668px; height: 865px;
    background: var(--paper);
    box-shadow: 0 4px 18px rgba(0,0,0,0.08);
  }
  .brand {
    position: absolute; left: 48px; top: 44px;
    display: flex; align-items: center; gap: 10px;
  }
  .brand-mark { width: 26px; height: 26px; background: var(--navy); }
  .brand-name {
    color: var(--navy); font-weight: 700; font-size: 30px; letter-spacing: 0.5px;
  }
  .dot-field {
    position: absolute; right: 0; top: 70px;
    width: 250px; height: 200px;
    background: linear-gradient(215deg, var(--dot-grey) 0%, rgba(220,220,223,0.45) 45%, rgba(255,255,255,0) 85%);
  }
  .footer {
    position: absolute; left: 40px; right: 40px; bottom: 36px;
  }
  .locations {
    display: flex; justify-content: space-between;
    padding: 0 8px;
  }
  .location { display: flex; gap: 7px; color: var(--navy); }
  .pin { width: 13px; height: 13px; flex: none; margin-top: 1px; }
  .location-name { font-size: 10.5px; margin-bottom: 3px; white-space: nowrap; }
  .location-line { font-size: 8px; line-height: 1.35; color: var(--blue); white-space: nowrap; }
  .rule { display: block; width: 100%; height: 28px; margin-top: 8px; }
  .contact {
    display: flex; justify-content: center; gap: 16px;
    margin-top: 4px; font-size: 10px; color: var(--navy);
  }
  .contact-item { display: flex; align-items: center; gap: 5px; }
  .contact-item svg { width: 10px; height: 10px; }
</style>
</head>
<body>
  <main class="letterhead">
    <header class="brand">
      <span class="brand-mark"></span>
      <span class="brand-name">PELMIR</span>
    </header>

    <div class="dot-field" role="img" aria-label="Soft grey dot pattern fading toward the page"></div>

    <footer class="footer">
      <div class="locations">
        <div class="location">
          <svg class="pin" viewBox="0 0 14 14"><rect x="0.5" y="0.5" width="13" height="13" fill="none" stroke="var(--sky)"/><path d="M7 3a2.6 2.6 0 0 0-2.6 2.6C4.4 7.6 7 11 7 11s2.6-3.4 2.6-5.4A2.6 2.6 0 0 0 7 3z" fill="var(--navy)"/><circle cx="7" cy="5.6" r="1" fill="#fff"/></svg>
          <div>
            <p class="location-name">PELMIR HQ</p>
            <p class="location-line">41827 Heron Bluff Lane, Suite 316</p>
            <p class="location-line">Fernhollow, CA 90418</p>
          </div>
        </div>
        <div class="location">
          <svg class="pin" viewBox="0 0 14 14"><rect x="0.5" y="0.5" width="13" height="13" fill="none" stroke="var(--sky)"/><path d="M7 3a2.6 2.6 0 0 0-2.6 2.6C4.4 7.6 7 11 7 11s2.6-3.4 2.6-5.4A2.6 2.6 0 0 0 7 3z" fill="var(--navy)"/><circle cx="7" cy="5.6" r="1" fill="#fff"/></svg>
          <div>
            <p class="location-name">PELMIR Elementary (K-5)</p>
            <p class="location-line">57314 Marbleton Ridge Road</p>
            <p class="location-line">Fernhollow, CA 90418</p>
          </div>
        </div>
        <div class="location">
          <svg class="pin" viewBox="0 0 14 14"><rect x="0.5" y="0.5" width="13" height="13" fill="none" stroke="var(--sky)"/><path d="M7 3a2.6 2.6 0 0 0-2.6 2.6C4.4 7.6 7 11 7 11s2.6-3.4 2.6-5.4A2.6 2.6 0 0 0 7 3z" fill="var(--navy)"/><circle cx="7" cy="5.6" r="1" fill="#fff"/></svg>
          <div>
            <p class="location-name">PELMIR College Prep (6-12)</p>
            <p class="location-line">46803 Sable Creek Way</p>
            <p class="location-line">Cresthaven Mesa, CA 90436</p>
          </div>
        </div>
      </div>

      <svg class="rule" viewBox="0 0 588 28" preserveAspectRatio="none">
        <path d="M0 4 Q294 34 588 18" fill="none" stroke="var(--blue)" stroke-width="1.6"/>
        <path d="M0 6 Q294 36 588 20" fill="none" stroke="var(--mist)" stroke-width="1"/>
      </svg>

      <div class="contact">
        <span class="contact-item">
          <svg viewBox="0 0 10 10"><path d="M2 1h2l1 2.3-1.2.9a5.5 5.5 0 0 0 2 2l.9-1.2L9 6v2a1 1 0 0 1-1 1A7 7 0 0 1 1 2a1 1 0 0 1 1-1z" fill="var(--sky)"/></svg>
          (555) 555-0147
        </span>
        <span class="contact-item">
          <svg viewBox="0 0 10 10"><circle cx="5" cy="5" r="4.3" fill="none" stroke="var(--sky)" stroke-width="1.1"/><circle cx="5" cy="5" r="1.6" fill="var(--sky)"/></svg>
          www.pelmir-learn.example
        </span>
      </div>
    </footer>
  </main>
</body>
</html>
```